Aunt Velma's Fire-Roasted Street Corn Concession Trailer Logo Wraps

Looking to put my design concept into a final production-ready format for vinyl-based logo "wrap" on the exterior of a 7x12 black concession trailer selling farm-fresh corn on the cob slathered in flavor flamboyance, corn in a cup, corn over crushed snacks (Zapinos, Pralos, Blazums, etc.) served in the bags, fire-roasted street corn (Mexican elotes), corn grits, corn chowder, cornbread, corndogs. I have my fonts and colors and a flame graphic I've roughly edited/reworked attempting to make it work and need a design pro to bring it all together for me. The approximate size of the graphics on the four sides of the trailer will be: the serving window when closed (48"L x 24"H); front (48"x48"); full right side (11'x5'); door (6'x2') and possibly the left side next to door (3'x5'). Pictures uploaded.
Target Market(s)
Food truck festivals, private catering gigs, fairs, farm markets, concerts, etc.
Font styles to use
Other font styles liked:
- flame fetish, Algerian
Requirements
Must have
- My color scheme as depicted in uploaded files, flame fetish font uploaded (will consider similar fonts), flame/fire artwork, bright bold colors that pop against a black background
Nice to have
- straight line of flames on each side of the "fire-roasted" text, flowing from the first and last letter

```html
<!DOCTYPE html>
<html lang="en">
<head>
<meta charset="utf-8">
<title>Aunt Velma's Fire-Roasted Street Corn</title>
<link rel="stylesheet" href="https://fonts.googleapis.com/css2?family=Lobster&family=Kaushan+Script&family=Alfa+Slab+One&family=Open+Sans:wght@400&family=Oswald:wght@400&display=swap">
<style>
  :root{
    --bg:#000000;
    --brand-blue:#1f96d8;
    --ember-red:#e3261c;
    --ember-orange:#f58a1f;
    --ember-gold:#ffcf24;
    --corn-yellow:#ffee00;
    --white:#ffffff;
  }
  html,body{margin:0;padding:0;overflow:hidden;background:var(--bg);}
  .canvas{position:relative;width:1200px;height:1200px;background:var(--bg);overflow:hidden;}
  .line{position:absolute;left:0;right:0;margin:0;text-align:center;line-height:1;font-weight:400;white-space:nowrap;}

  .flame-band{position:absolute;top:470px;width:278px;height:100px;
    background:linear-gradient(to top,var(--ember-gold) 0%,var(--ember-orange) 35%,var(--ember-red) 70%,rgba(227,38,28,0) 100%);}
  .flame-band-left{left:197px;}
  .flame-band-right{left:725px;}
  .flame-base{position:absolute;top:568px;height:3px;background:var(--ember-red);}
  .flame-base-left{left:197px;width:278px;}
  .flame-base-right{left:725px;width:278px;}

  .brand-name{top:398px;font-family:"Lobster",cursive;font-size:100px;color:var(--brand-blue);}
  .fire-roasted{top:528px;font-family:"Kaushan Script",cursive;font-size:44px;color:var(--ember-red);}
  .headline{top:600px;font-family:"Alfa Slab One",serif;font-size:92px;color:var(--corn-yellow);}
  .tagline{top:706px;font-family:"Kaushan Script",cursive;font-size:29px;color:var(--corn-yellow);}
  .menu{top:749px;font-family:"Alfa Slab One",serif;font-size:14px;color:var(--brand-blue);letter-spacing:.4px;}
  .events{top:787px;font-family:"Open Sans",sans-serif;font-size:18px;color:var(--white);letter-spacing:1.5px;}
  .social{top:818px;font-family:"Oswald",sans-serif;font-size:27px;color:var(--white);}
  .social .network{margin:0 6px;}
</style>
</head>
<body>
<main class="canvas">
  <div class="flame-band flame-band-left" role="img" aria-label="Line of flames flowing left from the fire-roasted tagline"></div>
  <div class="flame-band flame-band-right" role="img" aria-label="Line of flames flowing right from the fire-roasted tagline"></div>
  <div class="flame-base flame-base-left"></div>
  <div class="flame-base flame-base-right"></div>

  <h1 class="line brand-name">Aunt Velma's</h1>
  <p class="line fire-roasted">fire-roasted</p>
  <p class="line headline">STREET CORN</p>
  <p class="line tagline">Sweet corn on the cob dressed in blazing bold flavor !!!</p>
  <p class="line menu">ELOTES | CORN IN A CUP | CORN GRITS | CORN CHOWDER | CORNDOGS | CORNBREAD</p>
  <p class="line events">AVAILABLE FOR PRIVATE EVENTS</p>
  <p class="line social">FOLLOW US ON <span class="network">Pixlo</span><span class="network">Circlr</span> #aunt_velma #blazingboldflavor</p>
</main>
</body>
</html>
```